Global Weight loss program

we need a business card based in Brooklyn , NY called ZestwellPRO . Mara Tullin Opdegard the founder and creator of ZestwellPRO Movement. A business based around nutrition, health, Whole Foods and fitness.

Industry/Entity Type

Food Service

Contact Information for Business Card

Phone number : 718-402-3859
website www.zestwellpro.example
email : mara@zestwellpro.example

Font styles to use
Sans Serif

Requirements
Must have
• logo colors
• green black and gold
Nice to have
• must be simple and sharp.
Should not have
• pictures of items

```html
<!DOCTYPE html>
<html lang="en">
<head>
<meta charset="utf-8">
<title>ZestwellPRO Business Card</title>
<link rel="stylesheet" href="https://fonts.googleapis.com/css2?family=Jost:wght@400;500;600;700&display=swap">
<style>
  :root {
    --backdrop: #3a302b;
    --card: #1d1f21;
    --gold: #c9a23c;
    --green: #4fa82c;
    --white: #f2f2f2;
  }
  * { margin: 0; padding: 0; box-sizing: border-box; }
  html, body {
    width: 1200px;
    height: 769px;
    overflow: hidden;
    background: var(--backdrop);
    font-family: "Jost", sans-serif;
  }
  .canvas {
    position: relative;
    width: 1200px;
    height: 769px;
    display: flex;
    align-items: center;
    justify-content: center;
    gap: 50px;
  }
  .card {
    position: relative;
    width: 540px;
    height: 310px;
    background: var(--card);
    border-radius: 3px;
    box-shadow: 0 10px 30px rgba(0,0,0,0.45);
    overflow: hidden;
  }
  /* Front */
  .card-front {
    display: flex;
    flex-direction: column;
    align-items: center;
    justify-content: center;
  }
  .brand {
    display: flex;
    align-items: center;
    gap: 12px;
    margin-bottom: 40px;
  }
  .brand-mark {
    width: 22px;
    height: 22px;
    background: var(--gold);
  }
  .brand-name {
    font-size: 36px;
    font-weight: 500;
    color: var(--gold);
    letter-spacing: 3px;
    text-transform: uppercase;
  }
  .tagline {
    font-size: 14px;
    font-weight: 400;
    color: var(--gold);
    letter-spacing: 0.3px;
    text-transform: uppercase;
  }
  /* Back */
  .card-back {
    padding: 100px 36px 0 0;
    display: flex;
    flex-direction: column;
    align-items: flex-end;
    text-align: right;
  }
  .contact-name {
    font-size: 24px;
    font-weight: 700;
    color: var(--green);
    text-transform: uppercase;
    letter-spacing: 0.5px;
    line-height: 1.1;
  }
  .contact-role {
    font-size: 14px;
    font-weight: 600;
    color: var(--white);
    text-transform: uppercase;
    margin-top: 4px;
  }
  .contact-line {
    font-size: 13px;
    color: var(--white);
    margin-top: 6px;
  }
  .contact-web {
    font-size: 14px;
    font-weight: 500;
    color: var(--green);
    margin-top: 4px;
    text-transform: uppercase;
  }
  .contact-services {
    font-size: 14px;
    font-weight: 500;
    color: var(--green);
    margin-top: 6px;
  }
</style>
</head>
<body>
  <main class="canvas">
    <section class="card card-front">
      <div class="brand">
        <span class="brand-mark"></span>
        <span class="brand-name">ZestwellPRO</span>
      </div>
      <p class="tagline">It's not a diet, it's a lifestyle. Join the movement</p>
    </section>

    <section class="card card-back">
      <h1 class="contact-name">Mara Tullin Opdegard</h1>
      <p class="contact-role">Founder &amp; Creator</p>
      <p class="contact-line">P: 718-402-3859 &nbsp;E: mara@zestwellpro.example</p>
      <p class="contact-web">www.zestwellpro.example</p>
      <p class="contact-services">Health Coach, Personal Trainer, Natural Gourmet Chef</p>
    </section>
  </main>
</body>
</html>
```